AUTO SPAREPART DISTRIBUTOR BUSINESS CARD

Our company need a business card design. We are a distributor and importer of car spareparts for ZOVA and MERLOTA car model. We would like the design with White color back ground and attractive color for the fonts and looks clean, simple and attractive.
We provide the company information and the brand logo (ZOVA, MERLOTA, DUP, 738) should be put on the business card.

Thank you

Target Market(s)

Auto spareparts retailer shop and supplier.

Industry/Entity Type

Business

Contact Information for Business Card

The front side of the business card only contain company informations, and the back side may be put the brand logo (ZOVA, MERLOTA, DUP AND 738).

Requirements
Must have
• On the back side ( the brand logo) position , should have a transparency world map picture ( i uploaded the world map picture sample ).
• Also, need to put some words of " AUTO PARTS DISTRIBUTOR " (may be put on any appropriate place).

```html
<!DOCTYPE html>
<html lang="en">
<head>
<meta charset="UTF-8">
<title>PT. Norvanta Inter Global – Business Card</title>
<link rel="stylesheet" href="https://fonts.googleapis.com/css2?family=Open+Sans:wght@400;600;700&display=swap">
<style>
  :root {
    --backdrop: #3b3532;
    --card: #ffffff;
    --ink: #2b2b2b;
    --ink-soft: #555555;
    --green: #7fb83a;
    --green-light: #9ccc5a;
    --grey: #8a8a8a;
    --map: #c9d3dc;
    --brand-blue: #1f5fb5;
    --brand-red: #d8232a;
  }
  * { margin: 0; padding: 0; box-sizing: border-box; }
  html, body {
    width: 1200px; height: 900px; overflow: hidden;
    background: var(--backdrop);
    font-family: "Open Sans", Arial, sans-serif;
  }
  .card {
    position: absolute;
    width: 525px; height: 300px;
    background: var(--card);
    border-radius: 3px;
    box-shadow: 0 10px 30px rgba(0,0,0,.45);
    overflow: hidden;
  }
  .card--front { left: 50px; top: 300px; }
  .card--back  { left: 625px; top: 300px; }

  /* Front */
  .mark {
    position: absolute; left: 40px; top: 0; width: 170px; height: 300px;
    display: flex; flex-direction: column; align-items: center; justify-content: center; gap: 14px;
  }
  .mark__square { width: 56px; height: 56px; background: var(--green); }
  .mark__name { color: var(--ink); font-weight: 700; font-size: 19px; letter-spacing: 1px; }
  .divider {
    position: absolute; left: 225px; top: 60px; width: 1px; height: 180px;
    background: linear-gradient(to bottom, transparent, var(--green), transparent);
  }
  .details { position: absolute; left: 245px; top: 52px; color: var(--ink); font-size: 12.5px; line-height: 1.35; }
  .details__name { color: var(--green); font-weight: 700; font-size: 17px; line-height: 1.1; }
  .details__role { font-size: 12px; margin-bottom: 14px; color: var(--ink-soft); }
  .details__address { margin-bottom: 14px; }
  .contacts { list-style: none; }
  .contacts li { display: flex; align-items: center; gap: 8px; height: 18px; }
  .contacts svg { width: 11px; height: 11px; fill: var(--green); flex: none; }

  /* Back */
  .world-map {
    position: absolute; left: 20px; right: 20px; top: 150px; height: 130px;
    border-radius: 50% / 40%;
    background: radial-gradient(ellipse at center, var(--map) 0%, rgba(201,211,220,.45) 55%, rgba(255,255,255,0) 75%);
    opacity: .7;
  }
  .company {
    position: absolute; left: 0; right: 0; top: 62px; text-align: center;
    color: var(--ink); font-weight: 700; font-size: 30px; letter-spacing: .5px;
  }
  .tagline {
    position: absolute; left: 0; right: 0; top: 110px; text-align: center;
    color: var(--green); font-size: 11px; letter-spacing: 4px; font-weight: 600;
  }
  .brands {
    position: absolute; left: 30px; right: 30px; bottom: 64px;
    display: flex; justify-content: space-around; align-items: center;
  }
  .brand { display: flex; flex-direction: column; align-items: center; gap: 2px; font-weight: 700; font-size: 15px; }
  .brand--merlota { color: var(--brand-blue); }
  .brand--zova { color: var(--brand-red); }
  .brand--dup { color: var(--ink); flex-direction: row; gap: 6px; }
  .brand--738 { color: var(--brand-red); }
  .brand__dot { width: 14px; height: 14px; background: var(--green); }
  .brand__sub { font-size: 7px; font-weight: 400; color: var(--brand-red); }
</style>
</head>
<body>
  <section class="card card--front">
    <div class="mark">
      <div class="mark__square"></div>
      <div class="mark__name">NORVANTA</div>
    </div>
    <div class="divider"></div>
    <div class="details">
      <div class="details__name">RAFI HARTONO</div>
      <div class="details__role">Director</div>
      <p class="details__address">Taman Sari Residence 4, Blok C-07 No.B-9,<br>Kembangan, Jakarta Barat,<br>Indonesia (11610).</p>
      <ul class="contacts">
        <li><svg viewBox="0 0 16 16"><path d="M3 1l3 3-2 2c1 2 3 4 5 5l2-2 3 3-2 3C7 14 2 9 1 3z"/></svg>+62-21-55038421</li>
        <li><svg viewBox="0 0 16 16"><rect x="2" y="6" width="12" height="8" rx="1"/><rect x="4" y="1" width="8" height="4"/></svg>+62-21-55038429</li>
        <li><svg viewBox="0 0 16 16"><rect x="4" y="1" width="8" height="14" rx="1.5"/></svg>+62-812740395</li>
        <li><svg viewBox="0 0 16 16"><path d="M1 3h14v10H1z"/></svg>norvanta-indonesia@mailbox.example</li>
        <li><svg viewBox="0 0 16 16"><circle cx="8" cy="8" r="7"/></svg>rafi.hart16</li>
      </ul>
    </div>
  </section>

  <section class="card card--back">
    <div class="world-map" role="img" aria-label="Transparent world map behind the partner brands"></div>
    <h1 class="company">PT. NORVANTA INTER GLOBAL</h1>
    <p class="tagline">AUTO PARTS DISTRIBUTOR</p>
    <div class="brands">
      <div class="brand brand--merlota">MERLOTA</div>
      <div class="brand brand--zova">ZOVA MOTORS</div>
      <div class="brand brand--dup"><span class="brand__dot"></span>DUP</div>
      <div class="brand brand--738">738<span class="brand__sub">738 Genuine Parts</span></div>
    </div>
  </section>
</body>
</html>
```